Criação de Logo e Papelaria (6 itens) para TREINAMENTO EM GESTAO
A empresa queria:
" É uma empresa que faz treinamentos de gestao, liderança, gestao em geral para empresários, funcionários e parceiros de negócio. "

```html
<!DOCTYPE html>
<html lang="pt-BR">
<head>
<meta charset="UTF-8">
<title>Valora — Pasta Institucional</title>
<link href="https://fonts.googleapis.com/css2?family=Cormorant+Garamond:wght@500&display=swap" rel="stylesheet">
<style>
  :root {
    --teal-deep: #17869c;
    --teal-mid: #3aa6b8;
    --teal-light: #66c3d1;
    --paper: #ffffff;
    --edge: #d9dde0;
    --gold: #c9ad7f;
    --canvas: #ffffff;
  }
  * { margin: 0; padding: 0; box-sizing: border-box; }
  html, body {
    width: 1200px; height: 1200px; overflow: hidden;
    background: var(--canvas);
  }
  .stage { position: relative; width: 1200px; height: 1200px; }
  .folder-art { position: absolute; inset: 0; }
  .address {
    position: absolute; left: 149px; width: 480px; top: 746px;
    text-align: center; color: var(--paper);
    font-family: "Cormorant Garamond", serif; font-weight: 500;
    font-size: 15px; letter-spacing: 1.8px; line-height: 19px;
    text-transform: uppercase;
  }
  .brand {
    position: absolute; left: 629px; width: 465px; top: 520px;
    display: flex; align-items: center; justify-content: center; gap: 16px;
  }
  .brand-dot {
    width: 20px; height: 20px; border-radius: 50%;
    background: var(--teal-mid); flex: none;
  }
  .brand-name {
    font-family: "Cormorant Garamond", serif; font-weight: 500;
    font-size: 52px; letter-spacing: 3px; color: var(--teal-mid);
    line-height: 1;
  }
  .pocket-brand {
    position: absolute; left: 419px; width: 120px; top: 1008px;
    text-align: center;
    font-family: "Cormorant Garamond", serif; font-weight: 500; font-size: 18px;
    letter-spacing: 1px; color: var(--teal-mid);
  }
  .base-rule {
    position: absolute; left: 0; right: 0; bottom: 8px; height: 4px;
    background: var(--gold);
  }
</style>
</head>
<body>
<main class="stage">
  <svg class="folder-art" width="1200" height="1200" viewBox="0 0 1200 1200">
    <defs>
      <linearGradient id="coverGradient" x1="0" y1="0" x2="1" y2="0">
        <stop offset="0" stop-color="#17869c"/>
        <stop offset="1" stop-color="#66c3d1"/>
      </linearGradient>
      <radialGradient id="motifGlow" cx="0.5" cy="0.5" r="0.5">
        <stop offset="0" stop-color="#ffffff" stop-opacity="0.4"/>
        <stop offset="1" stop-color="#ffffff" stop-opacity="0"/>
      </radialGradient>
    </defs>

    <rect class="panel-right" x="629" y="156" width="465" height="768"
          fill="#ffffff" stroke="#d9dde0" stroke-width="1.5"/>

    <path class="side-tab" d="M149 648 L128 660 L128 890 L149 902 Z"
          fill="#ffffff" stroke="#d9dde0" stroke-width="1.5"/>

    <path class="cover-pocket" d="M149 156 H629 V1068 H149 Z"
          fill="#ffffff" stroke="#d9dde0" stroke-width="1.5"/>
    <path class="cover-band"
          d="M149 156 H629 V940 C560 905 470 925 380 960 C300 990 220 985 149 965 Z"
          fill="url(#coverGradient)"/>

    <g role="img" aria-label="Ilustração decorativa de folhas e asas claras em voo">
      <ellipse cx="360" cy="380" rx="170" ry="210" fill="url(#motifGlow)"/>
    </g>
  </svg>

  <p class="address">
    Rua das Acácias nº 512 | 3º andar | sala 210<br>
    Botafogo | Rio de Janeiro | 22250040<br>
    contato@valora.com.br<br>
    www.valora.com.br
  </p>

  <div class="brand">
    <span class="brand-dot"></span>
    <span class="brand-name">VALORA</span>
  </div>

  <div class="pocket-brand">VALORA</div>

  <div class="base-rule"></div>
</main>
</body>
</html>
```